2-Sided Law Firm Business Card

This is the second phase of a law firm "rebrand project" in which I'm changing my firm's name to "Brackwood Law PLLC." The first phase was a logo contest -- I will be updating this project sometime tomorrow with the winning logo design.

The business card will need to include, on its reverse side, the firm's logo and tag line, "Legal Counsel for the Innovative Company," on a darker background whose color is consistent with the logo design.

The face of the card will need to include the firm's name (logo), website url, and phone number. It will also need to include, at the very least, the name of the attorney, the attorney's title, the attorney's email address, and the attorney's twitter feed. (I do not maintain a dedicated office and therefore the card does not need to specify a business address.) I will provide the actual contact information to the winning designer. Until then, you may use fictional data in suggesting your proposed design.

My firm specializes in representing startup companies. This means I routinely interact with young entrepreneurs and the (typically) older, more experienced investors who fund them. I need to appeal to the former without offending the latter. I'm interesting in conveying the idea that my firm is a credible alternative to larger, brand-name firms. I use these words in positioning my firm in this market: creative; flexible; fair; practical; experienced. The winning design needs to convey this idea.

I'm will also be re-working my website soon and will likely use noto sans and noto serif as my primary website fonts. I'd like the business card to use a font that is similar, but also compatible with the font used in the firm's logo.

Target Market(s)

Young entrepreneurs and older investors who collaborate in the formation and funding of high-tech startup companies located in the Pacific Northwest.

Industry/Entity Type

Law Firm

Font styles to use
Serif
Sans Serif

Requirements
Must have
• Firm logo, firm tag line, firm website url, firm phone number, attorney name, attorney title, attorney email address, and attorney twitter.

The attached pdf indicates kind of what I have in mind, recognizing that it is my amateur attempt at doing what I'm hoping the winning designer is able to do so much better.
Nice to have
• Adding a statement about my practice areas, if there's room, might be nice:

"General Counsel | Business Formation | Intellectual Property | Angel Investments & Venture Capital | Mergers & Acquisitions"

Also, I make it a point to meet with clients "by appointment only" in the following areas of Seattle: "Freemont | Pioneer Square | Redmond | South Lake Union." It might be worth including as well, but only if the card itself isn't too cramped. I favor "too simple" over "too informative."
Should not have
• Do NOT put the scales of justice anywhere on this business card. I am a business lawyer.

```html
<!DOCTYPE html>
<html lang="en">
<head>
<meta charset="utf-8">
<title>Brackwood Law PLLC – Business Card</title>
<link rel="stylesheet" href="https://fonts.googleapis.com/css2?family=Archivo+Narrow:wght@700&family=Questrial&display=swap">
<style>
  :root {
    --bg-light: #eceeee;
    --bg-mid: #c9cdcd;
    --navy: #0f1a33;
    --ink: #1b2233;
    --gold-light: #f6f1cf;
    --gold-mid: #d9c071;
    --gold-pale: #f4eedb;
    --gold-text: #d6bf78;
    --back-dark: #0a0e16;
    --back-blue: #0e2260;
  }
  * { margin: 0; padding: 0; box-sizing: border-box; }
  html, body { width: 1200px; height: 1000px; overflow: hidden; }
  body {
    background: radial-gradient(ellipse at 55% 45%, var(--bg-light) 0%, var(--bg-mid) 100%);
    font-family: "Questrial", sans-serif;
    color: var(--ink);
    position: relative;
  }
  .card {
    position: absolute;
    top: 362px;
    width: 480px;
    height: 275px;
    border-radius: 12px;
    overflow: hidden;
  }
  /* Front */
  .card-front {
    left: 90px;
    background: linear-gradient(160deg, var(--gold-light) 0%, var(--gold-mid) 55%, var(--gold-pale) 100%);
  }
  .firm-mark {
    position: absolute; left: 18px; top: 22px;
    display: flex; align-items: center; gap: 8px;
  }
  .mark-square { width: 38px; height: 38px; border: 3px solid var(--navy); border-radius: 5px; }
  .firm-name {
    font-family: "Archivo Narrow", sans-serif; font-weight: 700;
    font-size: 17px; color: var(--navy); line-height: 1;
  }
  .firm-url {
    display: block; margin-top: 5px;
    font-size: 9.5px; letter-spacing: 0.6px; color: var(--ink);
  }
  .phone {
    position: absolute; left: 286px; top: 34px;
    display: flex; align-items: center; gap: 6px;
    font-family: "Archivo Narrow", sans-serif; font-weight: 700;
    font-size: 16px; letter-spacing: 0.8px; color: var(--navy);
  }
  .attorney { position: absolute; left: 20px; top: 102px; }
  .attorney-name {
    font-size: 15px; font-weight: 700; font-variant: small-caps; letter-spacing: 1.2px;
    color: var(--navy); -webkit-text-stroke: 0.4px var(--navy);
  }
  .attorney-name::before { content: "•"; margin-right: 3px; }
  .attorney-title {
    margin: 4px 0 0 12px; font-size: 12px; font-variant: small-caps; letter-spacing: 0.8px;
  }
  .contact { position: absolute; left: 22px; top: 170px; list-style: none; }
  .contact li {
    display: flex; align-items: center; gap: 6px;
    font-size: 10px; font-variant: small-caps; letter-spacing: 0.7px; margin-bottom: 8px;
  }
  .social-dot { width: 11px; height: 11px; border-radius: 50%; background: var(--navy); }
  .divider {
    position: absolute; left: 228px; top: 78px; width: 3px; height: 162px;
    background: var(--navy); border-radius: 2px;
  }
  .practice-areas { position: absolute; left: 246px; top: 106px; list-style: none; }
  .practice-areas li {
    font-size: 10px; font-variant: small-caps; letter-spacing: 0.6px; margin-bottom: 6px;
  }
  .practice-areas li::before {
    content: ""; display: inline-block; width: 5px; height: 5px; border-radius: 50%;
    background: var(--navy); margin-right: 6px; vertical-align: middle;
  }
  .locations {
    position: absolute; left: 0; right: 0; bottom: 15px; text-align: center;
    font-size: 10px; font-variant: small-caps; letter-spacing: 0.6px;
  }
  .locations .sep {
    display: inline-block; width: 5px; height: 5px; border-radius: 50%;
    background: var(--navy); margin: 0 4px; vertical-align: middle;
  }
  /* Back */
  .card-back {
    left: 630px;
    background: linear-gradient(110deg, var(--back-dark) 0%, #0c1430 55%, var(--back-blue) 100%);
    display: flex; flex-direction: column; align-items: center; justify-content: center;
  }
  .back-mark { display: flex; align-items: center; gap: 10px; margin-top: 40px; }
  .back-mark .mark-square { width: 24px; height: 24px; border-color: var(--gold-text); border-width: 2px; }
  .back-name {
    font-family: "Archivo Narrow", sans-serif; font-weight: 700;
    font-size: 20px; color: var(--gold-text);
  }
  .tagline {
    margin-top: 10px; font-size: 9px; font-variant: small-caps; letter-spacing: 1px;
    color: var(--gold-text);
  }
</style>
</head>
<body>
  <section class="card card-front" aria-label="Business card front">
    <div class="firm-mark">
      <span class="mark-square"></span>
      <div>
        <span class="firm-name">Brackwood Law PLLC.</span>
        <span class="firm-url">WWW.BRACKWOODLAWPLLC.COM</span>
      </div>
    </div>
    <div class="phone">
      <svg width="14" height="16" viewBox="0 0 24 24" aria-hidden="true"><path fill="#0f1a33" d="M6.6 10.8a15.1 15.1 0 0 0 6.6 6.6l2.2-2.2c.3-.3.7-.4 1-.2 1.1.4 2.3.6 3.6.6.6 0 1 .4 1 1V20c0 .6-.4 1-1 1A17 17 0 0 1 3 4c0-.6.4-1 1-1h3.5c.6 0 1 .4 1 1 0 1.3.2 2.5.6 3.6.1.3 0 .7-.2 1z"/></svg>
      425.555.0142
    </div>
    <div class="attorney">
      <p class="attorney-name">Evan R. Holt</p>
      <p class="attorney-title">Startup Attorney</p>
    </div>
    <ul class="contact">
      <li><span class="social-dot"></span>@evanholt</li>
      <li>
        <svg width="13" height="10" viewBox="0 0 13 10" aria-hidden="true"><rect x="0.5" y="0.5" width="12" height="9" fill="#0f1a33"/><path d="M0.5 0.5 6.5 5.5 12.5 0.5" fill="none" stroke="#e6d59a" stroke-width="1"/></svg>
        evan@brackwoodlawpllc.com
      </li>
    </ul>
    <span class="divider"></span>
    <ul class="practice-areas">
      <li>General Counsel</li>
      <li>Business Formation</li>
      <li>Intellectual Property</li>
      <li>Angel Investments &amp; Venture Capital</li>
      <li>Mergers &amp; Acquisitions</li>
    </ul>
    <p class="locations">Freemont<span class="sep"></span>Pioneer Square<span class="sep"></span>Redmond<span class="sep"></span>South Lake Union</p>
  </section>

  <section class="card card-back" aria-label="Business card back">
    <div class="back-mark">
      <span class="mark-square"></span>
      <span class="back-name">Brackwood Law PLLC.</span>
    </div>
    <p class="tagline">Legal Counsel for the Innovative Company</p>
  </section>
</body>
</html>
```